Birchway Appliance Care - Repair Plan Paperwork

Home Appliance Repair Agent and Repair Plan providing services to consumers' home appliances.

Pages Layout Guideline:
1) Introduction to BAC / Plan Schedule / Repair Plan Ref
2) Appliance Type / Model / Age / Cost of appliance within Repair Plan / Payment Schedule / Payment Dates / Amounts
3) Terms & Conditions

- Will also want a flyer design to go inside with the paperwork to market savings by adding additional products.

I have uploaded the logo, letterheads and website pages so you get a feel of the branding / design we use throughout.

```html
<!DOCTYPE html>
<html lang="en">
<head>
<meta charset="utf-8">
<title>Birchway Appliance Care – Repair Plan Paperwork</title>
<link rel="stylesheet" href="https://fonts.googleapis.com/css2?family=Montserrat:wght@400;600;700&family=PT+Sans:wght@400;700&display=swap">
<style>
  :root{
    --backdrop:#898a89;
    --paper:#ffffff;
    --pale-teal:#d8f0f3;
    --mid-teal:#9fdbe2;
    --deep-teal:#36b3c3;
    --orange:#ef5a28;
    --ink:#1f1f1f;
    --body-ink:#3a3a3a;
    --brand-grey:#6f7072;
    --row-grey:#e6e6e6;
    --row-dark:#b9b9b9;
    --photo-a:#c9ccd0;
    --photo-b:#5a5e66;
  }
  *{box-sizing:border-box;margin:0;padding:0}
  html,body{width:1200px;height:1200px;overflow:hidden;background:var(--backdrop)}
  .spread{position:relative;width:1200px;height:1200px}
  .page{
    position:absolute;left:470px;width:418px;height:542px;
    transform:scale(0.622);transform-origin:0 0;
    background:var(--paper);overflow:hidden;
    font-family:"PT Sans",sans-serif;color:var(--body-ink);
  }
  .page--cover{top:83px}
  .page--intro{top:432px}
  .page--schedule{top:781px}
  .page-art{position:absolute;inset:0;width:418px;height:542px}
  .brand{
    position:absolute;left:20px;top:22px;display:flex;align-items:center;gap:5px;
    font-family:"Montserrat",sans-serif;font-weight:600;font-size:11px;
    color:var(--brand-grey);letter-spacing:.2px;
  }
  .brand__dot{width:9px;height:9px;border-radius:50%;background:var(--brand-grey)}
  .cover-title{
    position:absolute;left:113px;top:137px;
    font-family:"Montserrat",sans-serif;font-weight:400;font-size:25px;line-height:27px;
    color:var(--ink);letter-spacing:.3px;
  }
  .cover-subtitle{
    position:absolute;left:113px;top:194px;
    font-family:"Montserrat",sans-serif;font-weight:700;font-size:13px;color:var(--orange);
  }
  .portrait{
    position:absolute;left:33px;top:99px;width:114px;height:114px;border-radius:50%;
    background:radial-gradient(circle at 50% 40%,#eceef0,#c4c8cc);
  }
  .section-title{
    font-family:"PT Sans",sans-serif;font-weight:700;font-size:13px;line-height:14px;color:var(--orange);
  }
  .intro-title{position:absolute;left:174px;top:124px}
  .body-copy{font-size:7px;line-height:10.4px;color:var(--body-ink)}
  .body-copy p+p{margin-top:8px}
  .intro-aside{position:absolute;left:28px;top:222px;width:128px}
  .intro-main{position:absolute;left:174px;top:165px;width:216px}
  .folio{
    position:absolute;left:373px;top:518px;height:24px;border-left:1px solid var(--ink);
    padding:4px 0 0 10px;font-weight:700;font-size:9px;color:var(--ink);
  }
  .schedule-title{position:absolute;right:29px;top:64px}
  .schedule{position:absolute;left:28px;top:92px;width:361px;list-style:none}
  .schedule__row{
    height:12.5px;margin-bottom:10.3px;background:var(--row-grey);
    font-size:6.5px;line-height:12.5px;padding-left:10px;color:var(--ink);text-transform:uppercase;
  }
  .schedule__row--weekend{background:var(--row-dark)}
  .notes{position:absolute;top:419px;width:165px}
  .notes--left{left:28px}
  .notes--right{left:223px}
</style>
</head>
<body>
<main class="spread">

  <!-- Cover -->
  <section class="page page--cover">
    <svg class="page-art" viewBox="0 0 418 542" aria-hidden="true">
      <polygon points="0,138 418,66 418,220 0,316" fill="var(--pale-teal)"/>
      <polygon points="0,316 418,220 418,236 0,332" fill="var(--mid-teal)"/>
    </svg>
    <svg class="page-art" viewBox="0 0 418 542" role="img" aria-label="Photo of a technician in blue overalls repairing a refrigerator in a modern kitchen">
      <defs>
        <linearGradient id="coverPhoto" x1="0" y1="0" x2="1" y2="1">
          <stop offset="0" stop-color="var(--photo-b)"/>
          <stop offset=".45" stop-color="var(--photo-a)"/>
          <stop offset="1" stop-color="#eef0f1"/>
        </linearGradient>
      </defs>
      <polygon points="0,332 418,236 418,542 0,542" fill="url(#coverPhoto)"/>
    </svg>
    <svg class="page-art" viewBox="0 0 418 542" aria-hidden="true">
      <polygon points="240,542 418,498 418,542" fill="var(--deep-teal)"/>
    </svg>
    <div class="brand"><span class="brand__dot"></span>Birchway Appliance Care</div>
    <h1 class="cover-title">BIRCHWAY<br>APPLIANCE CARE</h1>
    <p class="cover-subtitle">Repair Plan Paperwork</p>
  </section>

  <!-- Introduction -->
  <section class="page page--intro">
    <svg class="page-art" viewBox="0 0 418 542" aria-hidden="true">
      <polygon points="0,364 418,290 418,542 0,542" fill="var(--pale-teal)"/>
    </svg>
    <div class="brand"><span class="brand__dot"></span>Birchway Appliance Care</div>
    <div class="portrait" role="img" aria-label="Portrait photo of a smiling customer service adviser holding a laptop"></div>
    <div class="intro-aside body-copy">
      <p>Lorem ipsum dolor sit amet, consectetur adipiscing elit. Fusce sit amet tincidunt dui. Maecenas fringilla nibh vel mi interdum, sit amet scelerisque elit fringilla. Curabitur non convallis augue. Sed sit amet dapibus risus. Sed vitae urna a metus iaculis dignissim. Suspendisse tincidunt orci vitae turpis facilisis ultrices. Vivamus pharetra mollis purus.</p>
    </div>
    <h2 class="section-title intro-title">Introduction<br>to BAC</h2>
    <div class="intro-main body-copy">
      <p>Vestibulum ante ipsum primis in faucibus orci luctus et ultrices posuere cubilia curae; Nullam consectetur arcu nec nisi lacinia aliquam non in eros. Nam eros purus, dignissim quis tellus ac, egestas vulputate ex. Duis rutrum, nisl quis ornare pulvinar, metus lacus dictum nunc, sed ullamcorper dolor lacus vel nunc. Cras ex purus, commodo a mi in, aliquam maximus felis. Class aptent taciti sociosqu ad litora torquent per conubia nostra, per inceptos himenaeos. Suspendisse sit amet nibh eu velit condimentum tincidunt. Vivamus mattis a urna eget venenatis. Praesent fringilla risus in pulvinar egestas. Sed dignissim vulputate mauris. Fusce molestie libero aliquam enim malesuada, sit amet porta tortor luctus. Interdum et malesuada fames ac ante ipsum primis in faucibus. In vitae quam dolor.</p>
      <p>Aenean laoreet pretium sapien, quis bibendum ex volutpat eget. Donec mattis consequat convallis. Curabitur orci eros, blandit at quam in, ornare elementum nulla. Praesent iaculis neque vitae justo rutrum tristique. Integer sed ex vel justo posuere bibendum. Nullam convallis scelerisque quam id tincidunt. Nulla posuere, dolor facilisis euismod interdum, elit enim tincidunt odio, ac ullamcorper elit ligula egestas nibh. Nunc justo purus, hendrerit vel nisl a, egestas fringilla mi. Praesent ac lectus neque. Fusce pulvinar augue non sapien tincidunt, id blandit lacus malesuada. Interdum et malesuada fames potenti. Nulla tristique faucibus mi non aliquam.</p>
      <p>Etiam a massa ante. Proin hendrerit eleifend turpis, sed varius massa fermentum a. Nunc erat orci, laoreet ut ex et, volutpat eleifend tellus. Donec quis mauris nisl. In hac habitasse platea dictumst. Quisque tortor. Etiam et tempor tellus, sed scelerisque velit.</p>
    </div>
    <div class="folio">2</div>
  </section>

  <!-- Plan schedule -->
  <section class="page page--schedule">
    <svg class="page-art" viewBox="0 0 418 542" aria-hidden="true">
      <polygon points="0,362 418,290 418,542 0,542" fill="var(--pale-teal)"/>
      <rect x="20" y="84" width="376" height="327" fill="var(--paper)"/>
    </svg>
    <div class="brand"><span class="brand__dot"></span>Birchway Appliance Care</div>
    <h2 class="section-title schedule-title">Plan Schedule</h2>
    <ol class="schedule">
      <li class="schedule__row">Monday</li>
      <li class="schedule__row">Tuesday</li>
      <li class="schedule__row">Wednesday</li>
      <li class="schedule__row">Thursday</li>
      <li class="schedule__row">Friday</li>
      <li class="schedule__row">Saturday</li>
      <li class="schedule__row schedule__row--weekend">Sunday</li>
      <li class="schedule__row">Monday</li>
      <li class="schedule__row">Tuesday</li>
      <li class="schedule__row">Wednesday</li>
      <li class="schedule__row">Thursday</li>
      <li class="schedule__row">Friday</li>
      <li class="schedule__row">Saturday</li>
      <li class="schedule__row schedule__row--weekend">Sunday</li>
    </ol>
    <div class="notes notes--left body-copy">
      <p>Lorem ipsum dolor sit amet, consectetur adipiscing elit. Fusce sit amet tincidunt dui. Maecenas fringilla nibh vel mi interdum, sit amet scelerisque elit fringilla. Curabitur non convallis augue. Sed sit amet dapibus risus. Sed vitae urna a metus iaculis dignissim.</p>
      <p>Suspendisse tincidunt orci vitae turpis facilisis ultrices. Vivamus pharetra mollis purus.</p>
    </div>
    <div class="notes notes--right body-copy">
      <p>Vestibulum ante ipsum primis in faucibus orci luctus et ultrices posuere cubilia curae; Nullam consectetur arcu nec nisi lacinia aliquam non in eros. Nam eros purus, divamus mattis a urna eget venenatis. Praesent et malesuada fames ac ante ipsum primis in faucibus. In vitae quam dolor.</p>
    </div>
    <div class="folio">4</div>
  </section>

</main>
</body>
</html>
```